App Design for FlavorTrek

We need an app design for a new app called FlavorTrek, which is an app designed to inspire exploration through personalized recipe generation, local restaurant discoveries, and a vibrant community platform. It caters to food enthusiasts looking to explore global cuisines or find the best local dining spots, offering a premium experience with selected features available for free.

-------UPDATED-----
This app will be AI Driven and may not be heavily dependent on media (images,videos) at first, especially for the Recipe generator feature. Our goal is to still have attractive UI. The core functionalities we are looking are the following
1. Recipe Generator: Either user choose a specific cuisine(italian,spanish), or user inputs ingredients and get recipe, or get recipe for different occasions (xmas, thanksgiving ) and get a randomly get recipe to cook, plain simple. We expect the recipes to be displayed in clear and not too generic manner starting with ingredients and expected duration at top and then step by step guide. We also intend to enable premium users to have playful action button or icon to get unlimited recipes generated until they find what they like and also have save for later feature. These premium features should be disabled for free users and prompted to subscribe if they click them with nice popup
2. Restaurant Recommendation - will have selected pictures and will be based on inputs such as zip code and other filters such as cousine types. Premium users can filter by price range, get unlimited recommendation, see actual price range in the recommendation and can save for later where they can find it later. Free users cannot filter by price (disabled) and should see it hidden in the recommendation
3. Meal Planning - will include just simple and random meal plan with just one button or limited interaction for free, users need to subscribe to get features such as customized plan such as considering allergies or diet preferences. Premium users can also get a shopping checklist of ingredients for weekly meal preps and their step by step guide for each meal recipe.
2. Community Sharing: users can view posts and engage with community content
Updates

Hello Designers,

The initial price was not fair for the work. So I have increased it. There will also be $50-100 bonus for those who come up with great designs or for those who incorporate interesting stuff. Thank you! Much appreciated 🙏

Colors
0054AA
0677BA
7BADD7
CADEEF
E8F1F8
0094D4
00A9DD
6FCCEA
C7EBF8
E9F6FB
00AB8E
00BBA5
67D7C9
C6EFE9
E9F9F6
FFC000
F8CF3A
FAE287
FDF2CF
FEFAEE
F0912C
F2A743
F7CA91
FBE8D2
FDF5EE
EE7325
F08F49
F5BC92
FAE3D3
FDF4ED
A7469A
B969AE
D3A5CF
EDDBEB
F8F0F9
6B429C
8869AF
B7A5CE
E3DAEB
F3F0F8

```html
<!DOCTYPE html>
<html lang="en">
<head>
<meta charset="utf-8">
<title>FlavorTrek – App Screens</title>
<link href="https://fonts.googleapis.com/css2?family=Outfit:wght@400;500;600&display=swap" rel="stylesheet">
<style>
:root{
  --page:#ffffff;
  --screen:#fdf9f4;
  --orange:#f4622f;
  --orange-soft:#fdeee6;
  --orange-tint:#fbdcc6;
  --cream:#fdf0d8;
  --cream-line:#f8ead4;
  --ink:#2b2b2b;
  --ink-soft:#4a4a4a;
  --muted:#8d8a86;
  --line:#efe6da;
  --dark:#131a2a;
  --photo-warm-a:#c8693a;
  --photo-warm-b:#5a3522;
}
*{box-sizing:border-box;margin:0;padding:0}
html,body{width:1200px;height:851px;overflow:hidden;background:var(--page)}
body{position:relative;font-family:'Outfit',sans-serif;color:var(--ink)}
.screen{
  position:absolute;top:73px;width:371px;background:var(--screen);
  border-radius:40px;overflow:hidden;transform:scale(.5236);transform-origin:0 0;
  box-shadow:0 0 0 1px #eee3d6;
}
.screen > *{position:absolute}
.s-welcome{left:77px;height:568px}
.s-recipes{left:290px;height:1225px}
.s-detail{left:502px;height:872px}
.s-restaurant{left:715px;height:1075px}
.s-meal{left:927px;height:1336px}

.status{top:18px;left:23px;right:23px;height:20px;display:flex;justify-content:space-between;align-items:center;font-size:14px;font-weight:600}
.status svg{width:40px;height:14px}

.avatar{left:17px;top:58px;width:42px;height:42px;border-radius:50%;background:linear-gradient(135deg,#8aa0b4,#6d5a4b)}
.crown{left:282px;top:68px;width:20px;height:20px;color:var(--orange)}
.menu-btn{left:313px;top:58px;width:42px;height:42px;border-radius:50%;background:var(--orange);display:flex;align-items:center;justify-content:center}
.menu-btn svg{width:18px;height:14px}

.label{left:17px;font-size:15px;font-weight:500;color:var(--ink)}
.group{left:17px;width:336px;border:1.5px solid var(--cream-line);border-radius:24px}
.field{left:24px;width:322px;height:44px;border-radius:22px;background:var(--cream);font-size:13px;color:var(--ink-soft);display:flex;align-items:center;padding-left:20px}
.field.is-placeholder{color:var(--muted)}
.chip{height:42px;border-radius:21px;background:var(--cream);font-size:13px;font-weight:500;display:flex;align-items:center;justify-content:center;color:var(--ink-soft)}
.chip .dash{color:var(--orange);margin-right:6px}
.chip.is-active{background:var(--orange-tint);border:1.5px solid #f3a37a;color:var(--ink);font-weight:600}

.btn{height:48px;border-radius:24px;font-size:15px;font-weight:600;display:flex;align-items:center;justify-content:center;gap:8px}
.btn svg{width:18px;height:18px}
.btn--fill{background:var(--orange);color:#fff}
.btn--outline{border:1.5px solid var(--orange);color:var(--orange);background:#fff}
.btn--soft{border:2px solid var(--orange);color:var(--orange);background:var(--orange-soft)}

.photo{border-radius:12px;background:linear-gradient(135deg,var(--photo-warm-a),var(--photo-warm-b))}
.photo--greens{background:linear-gradient(135deg,#3d5b2a,#b8562c 60%,#2a1a12)}
.photo--dark{background:linear-gradient(135deg,#2a1f1a,#c68a4a 70%,#e9c9a0)}
.photo--room{background:linear-gradient(160deg,#6b3a22,#c48a5c 55%,#efe6dc)}
.photo--noodle{background:radial-gradient(circle at 60% 55%,#f0b64a,#d86a32 45%,#e8e4de 80%)}

.r-title{font-size:17px;font-weight:600}
.r-sub{font-size:11px;color:var(--muted)}
.r-stats{display:flex;gap:26px;font-size:11px;color:var(--ink-soft)}
.stat{display:flex;align-items:center;gap:4px}
.stat svg{width:13px;height:13px;color:var(--orange)}

.box{left:17px;width:337px;border:1.5px solid var(--line);border-radius:14px;background:var(--screen)}
.stats-row{display:flex;justify-content:space-around;align-items:center;font-size:13px;color:var(--ink-soft)}
.stats-row .stat svg{width:16px;height:16px}
.box h4{font-size:15px;font-weight:500;margin:0 0 8px}
.box ul{list-style:none;font-size:13px;color:var(--ink-soft);line-height:26px;margin-bottom:12px}
.box li::before{content:"•";margin:0 8px 0 6px;color:var(--ink-soft)}
.box p{font-size:13px;color:var(--ink-soft);line-height:16px}

.d-title{left:17px;font-size:23px;font-weight:600}
.d-sub{left:17px;font-size:13px;color:var(--ink-soft)}

.tabbar{left:0;right:0;border-top:1px solid var(--line);display:flex;justify-content:space-around;padding:14px 18px 0}
.tab{width:70px;display:flex;flex-direction:column;align-items:center;gap:4px;font-size:11px;color:#aaa6a0}
.tab svg{width:20px;height:20px}
.tab.is-active{color:var(--orange);font-weight:500}

.hello{left:0;right:0;top:350px;text-align:center;font-size:27px;font-weight:500;line-height:31px;color:#3b3b3b}
.quick{top:428px;width:105px;height:105px;border-radius:50%;background:var(--cream);display:flex;flex-direction:column;align-items:center;justify-content:center;gap:8px;color:var(--orange);font-size:12px;font-weight:500}
.quick svg{width:30px;height:30px}

.locked{opacity:.45;filter:blur(.6px)}
.tooltip{left:100px;top:422px;width:170px;height:45px;border-radius:10px;background:var(--dark);color:#fff;font-size:10px;line-height:13px;display:flex;align-items:center;gap:10px;padding:0 14px}
.tooltip svg{width:18px;height:18px;color:var(--orange);flex:none}
.rest-card{left:17px;top:628px;width:337px;height:278px;border-radius:14px;overflow:hidden;background:#fdf6ec}
.rest-card .photo{position:absolute;left:0;top:0;width:100%;height:167px;border-radius:0}
</style>
</head>
<body>

<svg width="0" height="0" style="position:absolute">
  <symbol id="i-flame" viewBox="0 0 16 16"><path d="M8 1.5c.5 2.5 4 4 4 8a4 4 0 0 1-8 0c0-2 1-3 2-4 0 1.5.8 2.3 1.6 2.5C7 6 7.5 3.5 8 1.5Z" fill="none" stroke="currentColor" stroke-width="1.4" stroke-linejoin="round"/></symbol>
  <symbol id="i-clock" viewBox="0 0 16 16"><circle cx="8" cy="8" r="6.3" fill="none" stroke="currentColor" stroke-width="1.4"/><path d="M8 4.5V8l2.3 1.5" fill="none" stroke="currentColor" stroke-width="1.4" stroke-linecap="round"/></symbol>
  <symbol id="i-user" viewBox="0 0 16 16"><circle cx="8" cy="8" r="6.3" fill="none" stroke="currentColor" stroke-width="1.4"/><circle cx="8" cy="6.8" r="2" fill="none" stroke="currentColor" stroke-width="1.4"/><path d="M4.4 12.3c1-1.5 2.2-2 3.6-2s2.6.5 3.6 2" fill="none" stroke="currentColor" stroke-width="1.4"/></symbol>
  <symbol id="i-spark" viewBox="0 0 18 18"><path d="M3 15 11 7M12 2v3M10.5 3.5h3M15 6v2M14 7h2M6 3v2M5 4h2" fill="none" stroke="currentColor" stroke-width="1.5" stroke-linecap="round"/></symbol>
  <symbol id="i-lock" viewBox="0 0 18 18"><rect x="3.5" y="8" width="11" height="8" rx="2" fill="none" stroke="currentColor" stroke-width="1.5"/><path d="M6 8V5.5a3 3 0 0 1 6 0" fill="none" stroke="currentColor" stroke-width="1.5"/><circle cx="9" cy="12" r="1" fill="currentColor"/></symbol>
  <symbol id="i-crown" viewBox="0 0 20 20"><path d="M3 15h14M4 13 3 6l4 3 3-5 3 5 4-3-1 7H4Z" fill="none" stroke="currentColor" stroke-width="1.5" stroke-linejoin="round"/></symbol>
  <symbol id="i-recipes" viewBox="0 0 20 20"><rect x="3.5" y="2.5" width="13" height="15" rx="3" fill="none" stroke="currentColor" stroke-width="1.5"/><path d="M7 8h6M7 11.5h4" stroke="currentColor" stroke-width="1.5" stroke-linecap="round"/></symbol>
  <symbol id="i-rest" viewBox="0 0 20 20"><rect x="3.5" y="6" width="13" height="11.5" rx="2" fill="none" stroke="currentColor" stroke-width="1.5"/><path d="M6 6V3.5h8V6M7 12h6M10 9v3" fill="none" stroke="currentColor" stroke-width="1.5" stroke-linecap="round"/></symbol>
  <symbol id="i-meal" viewBox="0 0 20 20"><path d="M2.5 11h15a7.5 5 0 0 1-15 0ZM5 10a5 4 0 0 1 10 0M8 7l2 3 2-3" fill="none" stroke="currentColor" stroke-width="1.5" stroke-linejoin="round"/></symbol>
  <symbol id="i-comm" viewBox="0 0 20 20"><circle cx="8" cy="6.5" r="3" fill="none" stroke="currentColor" stroke-width="1.5"/><circle cx="14" cy="7.5" r="2.2" fill="none" stroke="currentColor" stroke-width="1.5"/><path d="M2.5 17c.6-3 2.8-4.5 5.5-4.5s4.9 1.5 5.5 4.5M14 12.5c2 0 3.3 1.3 3.7 3.5" fill="none" stroke="currentColor" stroke-width="1.5" stroke-linecap="round"/></symbol>
  <symbol id="i-star" viewBox="0 0 16 16"><path d="m8 1.5 2 4.3 4.6.5-3.4 3.1 1 4.6L8 11.7 3.8 14l1-4.6L1.4 6.3 6 5.8Z" fill="currentColor"/></symbol>
  <symbol id="i-pin" viewBox="0 0 16 16"><circle cx="8" cy="8" r="6.3" fill="none" stroke="currentColor" stroke-width="1.4"/><circle cx="8" cy="7" r="1.8" fill="none" stroke="currentColor" stroke-width="1.4"/><path d="M8 13V9" stroke="currentColor" stroke-width="1.4"/></symbol>
  <symbol id="i-coin" viewBox="0 0 16 16"><circle cx="8" cy="8" r="6.3" fill="none" stroke="currentColor" stroke-width="1.4"/><path d="M10 5.8C9.5 5.2 8.8 5 8 5c-1.2 0-2 .6-2 1.5C6 8.6 10 7.4 10 9.5c0 .9-.8 1.5-2 1.5-.9 0-1.6-.3-2-.9M8 4v8" fill="none" stroke="currentColor" stroke-width="1.3" stroke-linecap="round"/></symbol>
  <symbol id="i-status" viewBox="0 0 40 14"><path d="M4 5a7 7 0 0 1 10 0M6 7.5a4 4 0 0 1 6 0" fill="none" stroke="currentColor" stroke-width="1.4" stroke-linecap="round"/><circle cx="9" cy="10" r="1.2" fill="currentColor"/><rect x="22" y="3" width="15" height="8" rx="2.5" fill="none" stroke="currentColor" stroke-width="1.3"/><rect x="24" y="5" width="7" height="4" rx="1" fill="currentColor"/></symbol>
  <symbol id="i-menu" viewBox="0 0 18 14"><path d="M2 2h14M2 7h14M2 12h9" stroke="#fff" stroke-width="2" stroke-linecap="round"/></symbol>
</svg>

<!-- Welcome -->
<section class="screen s-welcome">
  <div class="status"><span>9:41</span><svg><use href="#i-status"/></svg></div>
  <div class="illus" role="img" aria-label="Line illustration of dishes, pans and ingredients seen from above" style="left:48px;top:65px;width:277px;height:255px;border-radius:50%;background:radial-gradient(circle,#fbdccb 0%,#fde9dc 55%,var(--screen) 75%)"></div>
  <h1 class="hello">Hi, What'd you like<br>today?</h1>
  <div class="quick" style="left:18px"><svg><use href="#i-recipes"/></svg>Get Recipes</div>
  <div class="quick" style="left:133px"><svg><use href="#i-rest"/></svg>Eat Out</div>
  <div class="quick" style="left:248px"><svg><use href="#i-meal"/></svg>Plan a meal</div>
</section>

<!-- Recipe generator -->
<section class="screen s-recipes">
  <div class="status"><span>9:41</span><svg><use href="#i-status"/></svg></div>
  <div class="avatar" role="img" aria-label="User profile photo"></div>
  <svg class="crown"><use href="#i-crown"/></svg>
  <div class="menu-btn"><svg><use href="#i-menu"/></svg></div>

  <div class="label" style="top:130px">Random recipe</div>
  <div class="btn btn--soft" style="left:17px;top:155px;width:336px"><svg><use href="#i-spark"/></svg>Surprise me</div>

  <div class="label" style="top:230px">Customise your recipe</div>
  <div class="group" style="top:257px;height:108px"></div>
  <div class="field is-placeholder" style="top:263px">Add ingredients</div>
  <div class="chip" style="left:24px;top:315px;width:66px"><span class="dash">-</span>Egg</div>
  <div class="chip" style="left:98px;top:315px;width:72px"><span class="dash">-</span>Flour</div>

  <div class="group" style="top:373px;height:110px"></div>
  <div class="field is-placeholder" style="top:379px">Choose &nbsp;Couisine</div>
  <div class="chip is-active" style="left:24px;top:431px;width:64px">Italian</div>
  <div class="chip" style="left:98px;top:431px;width:72px">Spanish</div>
  <div class="chip" style="left:180px;top:431px;width:62px">Indian</div>

  <div class="group" style="top:490px;height:56px"></div>
  <div class="field" style="top:496px">Choose different occasions</div>
  <div class="group" style="top:556px;height:56px"></div>
  <div class="field" style="top:562px">Avoid ingridients</div>

  <div class="btn btn--fill" style="left:17px;top:625px;width:336px"><svg><use href="#i-spark"/></svg>Get your recipe</div>

  <div class="label" style="top:718px">Recipe result</div>

  <div class="photo" role="img" aria-label="Pizza slices on a board" style="left:17px;top:742px;width:87px;height:87px"></div>
  <div class="r-title" style="left:117px;top:748px">Pizza Recipes 01</div>
  <div class="r-sub" style="left:117px;top:772px">Italian Cuisine</div>
  <div class="r-stats" style="left:117px;top:808px"><span class="stat"><svg><use href="#i-flame"/></svg>330 Cal</span><span class="stat"><svg><use href="#i-clock"/></svg>15 Min</span><span class="stat"><svg><use href="#i-user"/></svg>2 Pe</span></div>

  <div class="photo photo--greens" role="img" aria-label="Pizza topped with fresh greens" style="left:17px;top:842px;width:87px;height:87px"></div>
  <div class="r-title" style="left:117px;top:848px">Pizza Recipes 03</div>
  <div class="r-sub" style="left:117px;top:872px">Italian Cuisine</div>
  <div class="r-stats" style="left:117px;top:908px"><span class="stat"><svg><use href="#i-flame"/></svg>330 Cal</span><span class="stat"><svg><use href="#i-clock"/></svg>15 Min</span><span class="stat"><svg><use href="#i-user"/></svg>2 Pe</span></div>

  <div class="photo photo--dark" role="img" aria-label="Pizza with rolling pin on a dark table" style="left:17px;top:942px;width:87px;height:87px"></div>
  <div class="r-title" style="left:117px;top:948px">Pizza Recipes 02</div>
  <div class="r-sub" style="left:117px;top:972px">Italian Cuisine</div>
  <div class="r-stats" style="left:117px;top:1008px"><span class="stat"><svg><use href="#i-flame"/></svg>330 Cal</span><span class="stat"><svg><use href="#i-clock"/></svg>15 Min</span><span class="stat"><svg><use href="#i-user"/></svg>2 Pe</span></div>

  <div class="btn btn--fill" style="left:17px;top:1040px;width:336px;height:44px"><svg><use href="#i-lock"/></svg>Go premium to more recipies</div>

  <nav class="tabbar" style="top:1130px;height:95px">
    <div class="tab is-active"><svg><use href="#i-recipes"/></svg>Recipes</div>
    <div class="tab"><svg><use href="#i-rest"/></svg>Restaurant</div>
    <div class="tab"><svg><use href="#i-meal"/></svg>Meal</div>
    <div class="tab"><svg><use href="#i-comm"/></svg>Comm</div>
  </nav>
</section>

<!-- Recipe detail -->
<section class="screen s-detail">
  <div class="status"><span>9:41</span><svg><use href="#i-status"/></svg></div>
  <div style="left:17px;top:56px;display:flex;align-items:center;gap:8px;font-size:13px;color:var(--ink-soft)">
    <svg width="16" height="12" viewBox="0 0 16 12"><path d="M15 6H2M6 1 1 6l5 5" fill="none" stroke="currentColor" stroke-width="1.5" stroke-linecap="round"/></svg>Recipe detail
  </div>
  <div class="photo" role="img" aria-label="Close-up of pizza slices with peppers and a pizza cutter" style="left:17px;top:85px;width:337px;height:169px"></div>
  <div class="d-title" style="top:264px">Pizza Recipes 01</div>
  <div class="d-sub" style="top:296px">Italian Cousine</div>
  <div class="box stats-row" style="top:331px;height:46px">
    <span class="stat"><svg><use href="#i-flame"/></svg>330 Cal</span><span class="stat"><svg><use href="#i-clock"/></svg>15 MIn</span><span class="stat"><svg><use href="#i-user"/></svg>2 Per</span>
  </div>
  <div class="box" style="top:384px;height:294px;padding:14px 13px">
    <h4>Ingredients</h4>
    <ul><li>3 Egg</li><li>500g Flour</li><li>250Ml Water</li><li>3 Egg</li><li>500g Flour</li></ul>
    <h4>Spices</h4>
    <ul><li>3 Egg</li><li>500g Flour</li><li>250Ml Water</li></ul>
  </div>
  <div class="box" style="top:685px;height:103px;padding:14px 13px">
    <h4>Preparation</h4>
    <p>Lorem ipsum dolor sit amet, consectetur adipiscing elit, sed do eiusmod tempor incididunt ut labore et dolore magna aliqua.</p>
  </div>
  <div class="btn btn--fill" style="left:17px;top:798px;width:337px">Save later</div>
</section>

<!-- Restaurants -->
<section class="screen s-restaurant">
  <div class="status"><span>9:41</span><svg><use href="#i-status"/></svg></div>
  <div class="avatar" role="img" aria-label="User profile photo"></div>
  <svg class="crown"><use href="#i-crown"/></svg>
  <div class="menu-btn"><svg><use href="#i-menu"/></svg></div>

  <div class="label" style="top:130px">Let’s get you a place to eat</div>
  <div class="group" style="top:155px;height:46px;border:none"></div>
  <div class="field" style="left:17px;width:336px;top:155px">Add ingredients</div>

  <div class="group" style="top:207px;height:110px"></div>
  <div class="field" style="top:213px">Choose &nbsp;Couisine type</div>
  <div class="chip is-active" style="left:24px;top:265px;width:64px">Italian</div>
  <div class="chip" style="left:98px;top:265px;width:72px">Spanish</div>
  <div class="chip" style="left:180px;top:265px;width:62px">Indian</div>

  <div class="group" style="top:325px;height:56px"></div>
  <div class="field" style="top:331px">Choose different occasions</div>

  <div class="group locked" style="top:388px;height:112px"></div>
  <div class="field locked" style="left:17px;width:336px;top:392px">Max Distance</div>
  <div class="chip locked" style="left:24px;top:450px;width:80px">Min Price</div>
  <div class="chip locked" style="left:112px;top:450px;width:84px">Max Price</div>
  <div class="tooltip"><svg><use href="#i-lock"/></svg><span>Go premium to unlock these features</span></div>

  <div class="btn btn--fill" style="left:17px;top:511px;width:336px"><svg><use href="#i-spark"/></svg>Get your restaurant</div>

  <div class="label" style="top:603px">Nearby Restaurant</div>
  <div class="rest-card">
    <div class="photo photo--room" role="img" aria-label="Restaurant dining room with set tables and wooden chairs"></div>
    <div class="d-title" style="position:absolute;left:17px;top:180px;font-size:22px">Pizza Restaurant 01</div>
    <div class="d-sub" style="position:absolute;left:17px;top:210px">Address 1234 N St</div>
    <div class="stats-row" style="position:absolute;left:17px;top:246px;gap:38px;justify-content:flex-start">
      <span class="stat"><svg><use href="#i-star"/></svg>4.2 (30+)</span><span class="stat"><svg><use href="#i-pin"/></svg>2.5 Km</span><span class="stat"><svg><use href="#i-coin"/></svg>25-300</span>
    </div>
  </div>
  <div class="btn btn--fill" style="left:17px;top:919px;width:164px">Next</div>
  <div class="btn btn--outline" style="left:190px;top:919px;width:164px">Save later</div>

  <nav class="tabbar" style="top:1010px;height:65px">
    <div class="tab"><svg><use href="#i-recipes"/></svg>Recipes</div>
    <div class="tab is-active"><svg><use href="#i-rest"/></svg>Restaurant</div>
    <div class="tab"><svg><use href="#i-meal"/></svg>Meal</div>
    <div class="tab"><svg><use href="#i-comm"/></svg>Comm</div>
  </nav>
</section>

<!-- Meal prep -->
<section class="screen s-meal">
  <div class="status"><span>9:41</span><svg><use href="#i-status"/></svg></div>
  <div class="avatar" role="img" aria-label="User profile photo"></div>
  <svg class="crown"><use href="#i-crown"/></svg>
  <div class="menu-btn"><svg><use href="#i-menu"/></svg></div>

  <div class="label" style="top:130px">Meal prep</div>
  <div class="group" style="top:155px;height:110px"></div>
  <div class="field" style="top:162px">Choose meal prep duration</div>
  <div class="chip is-active" style="left:24px;top:214px;width:68px">2 Days</div>
  <div class="chip" style="left:100px;top:214px;width:68px">3 Days</div>
  <div class="chip" style="left:175px;top:214px;width:68px">5 Days</div>

  <div class="btn btn--fill" style="left:17px;top:275px;width:164px;height:46px;font-size:13px">I have Ingredients</div>
  <div class="btn btn--outline" style="left:190px;top:275px;width:164px;height:46px;font-size:13px;color:var(--ink);border-color:#f3b293">Generate Ingridients</div>

  <div class="group" style="top:352px;height:110px"></div>
  <div class="field is-placeholder" style="top:358px">Add ingredients</div>
  <div class="chip" style="left:24px;top:410px;width:66px"><span class="dash">-</span>Egg</div>
  <div class="chip" style="left:98px;top:410px;width:72px"><span class="dash">-</span>Flour</div>

  <div class="photo photo--noodle" role="img" aria-label="Bowl of noodle soup with herbs and chili" style="left:17px;top:469px;width:337px;height:168px"></div>
  <div class="d-title" style="top:647px">Noodle Recipes 01</div>
  <div class="d-sub" style="top:679px">Italian Cousine</div>
  <div class="box stats-row" style="top:715px;height:46px">
    <span class="stat"><svg><use href="#i-flame"/></svg>330 Cal</span><span class="stat"><svg><use href="#i-clock"/></svg>15 MIn</span><span class="stat"><svg><use href="#i-user"/></svg>2 Per</span>
  </div>
  <div class="box" style="top:768px;height:292px;padding:14px 13px">
    <h4>Ingredients</h4>
    <ul><li>3 Egg</li><li>500g Flour</li><li>250Ml Water</li><li>3 Egg</li><li>500g Flour</li></ul>
    <h4>Spices</h4>
    <ul><li>3 Egg</li><li>500g Flour</li><li>250Ml Water</li></ul>
  </div>
  <div class="box" style="top:1068px;height:102px;padding:14px 13px">
    <h4>Preparation</h4>
    <p>Lorem ipsum dolor sit amet, consectetur adipiscing elit, sed do eiusmod tempor incididunt ut labore et dolore magna aliqua.</p>
  </div>
  <div class="btn btn--fill" style="left:17px;top:1182px;width:164px">Get new</div>
  <div class="btn btn--outline" style="left:190px;top:1182px;width:164px">Save later</div>

  <nav class="tabbar" style="top:1275px;height:61px">
    <div class="tab"><svg><use href="#i-recipes"/></svg>Recipes</div>
    <div class="tab"><svg><use href="#i-rest"/></svg>Restaurant</div>
    <div class="tab is-active"><svg><use href="#i-meal"/></svg>Meal</div>
    <div class="tab"><svg><use href="#i-comm"/></svg>Comm</div>
  </nav>
</section>

</body>
</html>
```